Podcast Cover Art for Fast Growing Show (Ill include a gracious tip!)

This artwork is for "The Steadfast Fellow Show." The podcast is for men, and it's all about self-improvement, confidence, success, money, women and masculinity. It's for the guy who wants to improve himself. I'd like for my picture to be included — in black and white — and I want the text to read: "The Steadfast Fellow Show" and somewhere in there it'll say: "with Dale Prowen." I'm open to color schemes. The podcast is a little edgy so I'd like for that to be represented in the design. Thank you! (((Here's the podcast page if you wanna check it out: http://steadfastfellowshow.castorbit.net/)))

Target Market(s)

Men who want to attract women and improve their lives!

Font styles to use
Serif

Colors

Designer to choose colors to be used in the design.

Requirements
Must have
• My image in it (in black and white) and the two titles: "The Steadfast Fellow Show" and "with Dale Prowen"
Nice to have
• My logo in it somehow (which is the arrow looking logo attached below). I've also found that my image looks best in black and white and with a circular type cut out (although I'm open to different design ideas). I've attached my logo with a circular cut out below so you can see what I'm talking about.
Should not have
• Flowers. Teddy bears. ice cream.

```html
<!DOCTYPE html>
<html lang="en">
<head>
<meta charset="utf-8">
<title>The Steadfast Fellow Show — Cover Art</title>
<link rel="stylesheet" href="https://fonts.googleapis.com/css2?family=Montserrat:wght@800;900&family=Playfair+Display:wght@700;900&display=swap">
<style>
  :root {
    --ink: #08090f;
    --navy: #15224f;
    --navy-line: #1b2a60;
    --signal-red: #e0391b;
    --paper: #f1f2f6;
    --portrait-light: #d9dade;
    --portrait-dark: #3c3d42;
  }
  * { margin: 0; padding: 0; box-sizing: border-box; }
  html, body { width: 1200px; height: 1200px; overflow: hidden; background: var(--ink); }
  .cover {
    position: relative;
    width: 1200px;
    height: 1200px;
    overflow: hidden;
    background: var(--ink);
  }
  .name-pattern {
    position: absolute;
    inset: 0;
    width: 1200px;
    height: 1200px;
  }
  .name-pattern text {
    font-family: "Montserrat", sans-serif;
    font-weight: 900;
    font-size: 255px;
    letter-spacing: -4px;
  }
  .name-pattern .outline { fill: none; stroke: var(--navy-line); stroke-width: 3; }
  .name-pattern .solid { fill: var(--navy); }
  .portrait-cutout {
    position: absolute;
    left: 695px;
    top: 95px;
    width: 1000px;
    height: 1000px;
    border-radius: 50%;
    background: var(--paper);
    overflow: hidden;
  }
  .portrait-photo {
    position: absolute;
    left: 270px;
    top: 200px;
    width: 520px;
    height: 720px;
    border-radius: 46% 46% 30% 30%;
    background: linear-gradient(160deg, var(--portrait-light) 0%, #9c9da3 45%, var(--portrait-dark) 100%);
  }
  .title-band {
    position: absolute;
    background: var(--signal-red);
    color: var(--paper);
    font-family: "Playfair Display", serif;
    font-weight: 900;
    display: flex;
    align-items: center;
    justify-content: center;
    box-shadow: 10px 14px 14px rgba(0, 0, 0, 0.55);
    white-space: nowrap;
  }
  .band-top {
    left: 55px; top: 382px;
    width: 900px; height: 150px;
    transform: rotate(-13deg);
    font-size: 84px;
    letter-spacing: 1px;
  }
  .band-middle {
    left: 125px; top: 575px;
    width: 760px; height: 160px;
    transform: rotate(1.5deg);
    font-size: 100px;
    letter-spacing: 38px;
    padding-left: 38px;
  }
  .band-bottom {
    left: 175px; top: 735px;
    width: 760px; height: 230px;
    transform: rotate(-7deg);
    font-size: 150px;
    letter-spacing: 2px;
  }
  .host-mark {
    position: absolute;
    left: 24px;
    top: 1060px;
    display: flex;
    align-items: center;
    gap: 30px;
  }
  .host-mark .mark-square {
    width: 96px;
    height: 96px;
    border: 8px solid var(--paper);
  }
  .host-mark .host-name {
    font-family: "Playfair Display", serif;
    font-weight: 700;
    font-size: 70px;
    color: var(--paper);
    letter-spacing: 1px;
  }
</style>
</head>
<body>
  <main class="cover">
    <svg class="name-pattern" viewBox="0 0 1200 1200" aria-hidden="true">
      <text class="outline" x="-20" y="230">DALE PROWEN</text>
      <text class="solid" x="-140" y="470">PROWEN</text>
      <text class="outline" x="-240" y="700">DALE PROWEN</text>
      <text class="outline" x="-90" y="940">PROWEN</text>
      <text class="outline" x="-160" y="1180">DALE PROWEN</text>
    </svg>

    <div class="portrait-cutout">
      <div class="portrait-photo" role="img" aria-label="Black and white portrait of host Dale Prowen, hands steepled in front of his chin"></div>
    </div>

    <h1 class="show-title">
      <span class="title-band band-top">THE STEADFAST</span>
      <span class="title-band band-middle">FELLOW</span>
      <span class="title-band band-bottom">SHOW</span>
    </h1>

    <div class="host-mark">
      <span class="mark-square"></span>
      <span class="host-name">DALE PROWEN</span>
    </div>
  </main>
</body>
</html>
```